Flyer/Poster design required for volunteer activities

We need a STRIKING A4 Poster/Flyer advertising our conservation volunteer program activities which are currently happening in the area. This poster is to advertise the program once people have arrived on the island or to locals. The program covers 5 months, May-September 2019 and is focused on conservation. I have attached the following:
- a flyer which was previously created (QMR Habitat Helpers 2019 sm)to advertise the program - would prefer it has a similar striking resemblance, but not essential
- A mock up document 'HHQMR On Island Poster_2019_v2' with text -Logos-Images

Target Market(s)

Everyone interested in Environmental Adventure/Hiking/Citizen Science

Industry/Entity Type

Tourism

Font styles to use
Sans Serif

Requirements
Must have
• -A travel conservation focus
• -Must use 'QMR-Background Image' as the background to the design
• -The info of where to get more information and the social media details must be prominent

```html
<!DOCTYPE html>
<html lang="en">
<head>
<meta charset="utf-8">
<title>QMR Habitat Helpers – May to September 2019</title>
<link rel="stylesheet" href="https://fonts.googleapis.com/css2?family=Bebas+Neue&family=Poppins:wght@400;500&display=swap">
<style>
:root{
  --page:#9fc3d6;
  --navy:#0d4f9a;
  --deep:#12427f;
  --panel:rgba(22,78,160,.86);
  --yellow:#fdd55b;
  --white:#ffffff;
  --sky:#bfe0f2;
  --sea:#2f86c6;
}
*{margin:0;padding:0;box-sizing:border-box}
html,body{width:1200px;height:1200px;overflow:hidden;background:var(--page)}
.poster{
  position:absolute;left:196px;top:30px;width:948px;height:1338px;
  transform:scale(.852);transform-origin:0 0;overflow:hidden;
  font-family:"Poppins",sans-serif;color:var(--white);
  box-shadow:12px 14px 18px rgba(0,0,0,.25);
}
.backdrop{position:absolute;inset:0;
  background:
   linear-gradient(180deg,var(--sky) 0%,#8fc3e4 12%,#3d8ed0 24%,#2a7fc4 38%,transparent 55%),
   linear-gradient(100deg,#5f8a3e 0%,#7a9a4a 12%,#3a86c0 30%,#1d6cb6 55%,#12458a 100%);}
.abs{position:absolute}
.display{font-family:"Bebas Neue",sans-serif;line-height:1}
.title{left:52px;top:38px;font-size:112px;color:var(--navy);-webkit-text-stroke:2px var(--white);letter-spacing:1px}
.subtitle{left:52px;top:158px;font-size:76px;color:var(--navy);-webkit-text-stroke:2px var(--white)}
.dates{left:52px;top:244px;font-size:40px;color:var(--yellow)}
.badge{left:800px;top:48px;width:110px;height:110px;display:flex;align-items:center;justify-content:center}
.badge-ring{position:absolute;inset:0;border:3px solid var(--navy);border-radius:50%;background:rgba(255,255,255,.35)}
.badge-name{position:relative;font-family:"Bebas Neue",sans-serif;font-size:30px;color:var(--navy)}
.band{left:0;width:948px;background:var(--yellow);color:var(--deep);text-align:center}
.band-top{top:292px;height:72px;font-size:62px;padding-top:8px}
.join{left:0;width:948px;top:372px;text-align:center;font-size:46px;color:var(--yellow);-webkit-text-stroke:.5px var(--deep)}
.panel{background:var(--panel)}
.photo{border-radius:50%;border:8px solid var(--white)}
.head{border:3px solid var(--white);border-right:none;padding:6px 0 0 10px}
.head-box{background:var(--panel)}
.month{font-size:38px}
.week{font-size:14px;letter-spacing:.3px}
.topic{font-size:26px;line-height:1}
ul.list{list-style:none;font-size:14.2px;line-height:20.8px}
ul.list li{padding-left:12px;position:relative}
ul.list li::before{content:"";position:absolute;left:1px;top:8px;width:5px;height:5px;border-radius:50%;background:var(--white)}
.footer{top:1275px;height:57px;font-size:16px;padding-top:5px}
.social{display:flex;justify-content:center;gap:34px;margin-top:4px;font-size:15px}
.social span{display:flex;align-items:center;gap:8px}
.dot{width:16px;height:16px;background:var(--deep);border-radius:3px}
</style>
</head>
<body>
<div class="poster">
  <div class="backdrop" role="img" aria-label="Aerial photograph of the island's lagoon, beaches, forested hills and mountains"></div>

  <div class="abs display title">QUILL MARSH REEF</div>
  <div class="abs display subtitle">CONSERVATION VOLUNTEERS</div>
  <div class="abs display dates">MAY – SEPTEMBER 2019</div>
  <div class="abs badge"><div class="badge-ring"></div><span class="badge-name">HHQMR</span></div>

  <div class="abs band band-top display">BE INVOLVED IN PROTECTING PARADISE</div>
  <div class="abs display join">JOIN THE QMR HABITAT HELPERS PROGRAM 2019</div>

  <!-- Birds -->
  <div class="abs panel" style="left:80px;top:440px;width:378px;height:308px"></div>
  <div class="abs display" style="left:258px;top:448px">
    <div class="month">MAY 2019</div><div class="week">FEATURE WEEK: 19TH – 26TH MAY</div></div>
  <div class="abs head display topic" style="left:250px;top:500px;width:208px;height:64px">BIRDS OF<br>QUILL MARSH REEF</div>
  <div class="abs photo" role="img" aria-label="Photo of a grey seabird on a nest" style="left:80px;top:440px;width:170px;height:166px;background:radial-gradient(circle at 50% 45%,#8a8c88,#4f6b3a 70%)"></div>
  <ul class="abs list" style="left:86px;top:618px;width:370px">
    <li>Ocean bird watching boat trips</li>
    <li>Guided tours of Woodhen and Currawong quarters</li>
    <li>Weekly lectures at the Quill Marsh Reef Museum</li>
    <li>Weekly screenings of documentaries on Bird and Island Conservation projects</li>
    <li>Self guided land bird survey tours</li>
  </ul>

  <!-- Marine park -->
  <div class="abs panel" style="left:490px;top:440px;width:378px;height:308px"></div>
  <div class="abs display" style="left:504px;top:448px">
    <div class="month">MAY 2019</div><div class="week">FEATURE WEEK: 19TH – 26TH MAY</div></div>
  <div class="abs head display topic" style="left:490px;top:500px;width:210px;height:64px;border-left:none;border-right:3px solid #fff;padding-left:14px">QUILL MARSH REEF<br>MARINE PARK</div>
  <div class="abs photo" role="img" aria-label="Photo of a snorkeller recording data underwater" style="left:698px;top:440px;width:172px;height:166px;background:radial-gradient(circle at 50% 50%,#2e79b6,#16467d 75%)"></div>
  <ul class="abs list" style="left:504px;top:577px;width:360px">
    <li style="width:210px">Marine pest monitoring with marine park staff</li>
    <li>Marine plastic &amp; debris clean up activities</li>
    <li>Screenings of marine conservation documentaries at the museum</li>
    <li>Weekly lectures on Marine Life at the Quill Marsh Reef Museum</li>
    <li>Marine Activities with local operators</li>
  </ul>

  <!-- Invasive species -->
  <div class="abs panel" style="left:80px;top:765px;width:378px;height:240px"></div>
  <div class="abs display" style="left:82px;top:767px;width:150px;height:60px;border:3px solid #fff;font-size:27px;display:flex;align-items:center;justify-content:center">INVASIVE SPECIES</div>
  <div class="abs display" style="left:268px;top:772px">
    <div class="month">JULY 2019</div><div class="week">FEATURE WEEK: 21ST – 28TH JULY</div></div>
  <ul class="abs list" style="left:86px;top:837px;width:370px">
    <li>Guided walks to learn about the weed eradication program</li>
    <li>Weekly lectures on plants of Quill Marsh Reef</li>
    <li>Weekly screenings of documentaries on plant and island conservation projects</li>
    <li>Guided walks to Mount Garrow</li>
    <li>Local tour guides include commentaries on island plants</li>
  </ul>

  <!-- Invertebrates -->
  <div class="abs panel" style="left:490px;top:775px;width:378px;height:341px"></div>
  <div class="abs display" style="left:504px;top:780px">
    <div class="month">MAY 2019</div><div class="week">FEATURE WEEK: 19TH – 26TH MAY</div></div>
  <div class="abs head display topic" style="left:490px;top:832px;width:210px;height:64px;border-left:none;border-right:3px solid #fff;padding-left:14px">AMAZING<br>INVERTEBRATES</div>
  <div class="abs photo" role="img" aria-label="Photo of a stick insect resting on open hands" style="left:698px;top:773px;width:172px;height:166px;background:radial-gradient(circle at 50% 50%,#d9b7a2,#8a6d60 75%)"></div>
  <ul class="abs list" style="left:504px;top:906px;width:360px">
    <li style="width:210px">Guided night walks to learn about the island's invertebrates</li>
    <li>Weekly viewing and presentation of the Quill Marsh Phasmid</li>
    <li>Weekly lectures on invertebrates of Quill Marsh Reef at the museum</li>
    <li>Weekly lectures on Marine Life at the Quill Marsh Reef Museum</li>
    <li>Weekly screenings of documentaries on island conservation projects</li>
  </ul>

  <!-- September -->
  <div class="abs panel" style="left:250px;top:1022px;width:208px;height:121px"></div>
  <div class="abs display" style="left:255px;top:1026px">
    <div class="month">SEPTEMBER 2019</div><div class="week">FEATURE WEEK: 1ST – 8TH SEPTEMBER</div></div>
  <div class="abs head display topic" style="left:250px;top:1080px;width:208px;height:64px">PROTECTING<br>PARADISE</div>
  <div class="abs panel" style="left:80px;top:1145px;width:788px;height:97px"></div>
  <div class="abs photo" role="img" aria-label="Photo of a hiker on a clifftop overlooking the sea" style="left:80px;top:1022px;width:170px;height:166px;background:linear-gradient(180deg,#d8e6f0 0%,#6a9ccc 45%,#3f6a3a 75%)"></div>
  <ul class="abs list" style="left:86px;top:1153px;width:780px">
    <li style="margin-left:154px">Observational snorkel surveys with Marine Ecologists, to assess populations of Banded Anemonefish and other unique fish species</li>
    <li style="margin-top:2px">Guided snorkel and glass bottom boat tour to assess coral health within the Quill Marsh Reef Marine Park</li>
    <li>Guided walks to learn about the island's conservation history</li>
  </ul>

  <div class="abs band footer">
    <div>See the QMR visitor centre for more information about the QMR Habitat Helpers program for 2019</div>
    <div class="social"><span><i class="dot"></i>www.hhqmr.org/community</span><span><i class="dot" style="border-radius:50%"></i>photos @hhqmr</span></div>
  </div>
</div>
</body>
</html>
```